National Golf Software business needs banner ad designs

Our software company looks after golf clubs throughout the country. Our service specialises in membership billing for the clubs and tries to convince members to change from paying their fees upfront to monthly payment by direct debit. Simple catch cries like "spread the cost of your membership across the whole year", "let us help you make your membership affordable", "Ask you club how to spread the cost of your subs" etc. We are dealing with cost conscious clubs - not the top end of the market - and their members are also cost conscious. No good being too 'high brow'. We are also dealing with older members who are fearful of change and afraid of technology - we need to be safe and reassuring yet a great way to save up front costs. We need probably 5 to 10 banners that can rotate through on our website and on our mobile product.

Target Market(s)

Golfers, typically older and afraid of technology and afraid of direct debit. Existing members of golf clubs who have paid upfront for years and don't understand why they should pay a few dollars extra each month to split their payments. Sometimes their annual fees are quite low ($300 - $400) so they cannot justify the additional $3.50 per month surcharge for splitting their fees.

Industry/Entity Type

Golf Course

Requirements
Must have
• Make the member desire to spread the cost of their annual subscriptions. Safe, reliable, frees up their disposable income. Talk to the club to find out how. Safe and secure. Club administered.
Nice to have
• Option to call us directly on a 1300 582 916 number - they will still need to go back to the club to fill in and lodge the paperwork.
Should not have
• Cheesy, in your face, aggressive

```html
<!DOCTYPE html>
<html lang="en">
<head>
<meta charset="UTF-8">
<title>Spread the Cost – Golf Membership Banner</title>
<link rel="stylesheet" href="https://fonts.googleapis.com/css2?family=Oswald:wght@500;600;700&display=swap">
<style>
  :root {
    --sky-top: #6f6a55;
    --sky-glow: #e9d9a8;
    --horizon: #c7b57a;
    --grass-light: #8fb03a;
    --grass-mid: #5f8a1f;
    --grass-dark: #2c4610;
    --band-dark: rgba(20, 20, 14, 0.62);
    --band-light: rgba(255, 255, 255, 0.72);
    --gold-hi: #fff6c8;
    --gold-mid: #d9a92a;
    --gold-lo: #6b4a08;
    --silver-hi: #ffffff;
    --silver-lo: #8c8c84;
    --ink: #1b1b18;
    --callout-yellow: #f5e21a;
    --call-red: #ff1f1f;
  }
  * { margin: 0; padding: 0; box-sizing: border-box; }
  html, body { width: 1200px; height: 557px; overflow: hidden; background: #fff; }
  .banner {
    position: relative;
    width: 1200px;
    height: 557px;
    overflow: hidden;
    font-family: "Oswald", "Arial Narrow", sans-serif;
    text-transform: uppercase;
  }
  .banner__photo {
    position: absolute; inset: 0;
    background:
      radial-gradient(ellipse 60% 45% at 45% 38%, var(--sky-glow) 0%, rgba(233,217,168,0) 70%),
      linear-gradient(180deg, var(--sky-top) 0%, var(--horizon) 52%, var(--grass-light) 58%, var(--grass-mid) 75%, var(--grass-dark) 100%);
  }
  .band { position: absolute; display: flex; align-items: center; justify-content: center; }
  .headline {
    left: 277px; top: 37px; width: 643px; height: 86px;
    background: var(--band-dark);
  }
  .headline__text {
    font-size: 74px; font-weight: 700; letter-spacing: 3px; line-height: 1;
    background: linear-gradient(180deg, var(--gold-hi) 0%, var(--gold-mid) 50%, var(--gold-lo) 100%);
    -webkit-background-clip: text; background-clip: text; color: transparent;
    filter: drop-shadow(2px 3px 2px rgba(0,0,0,0.7));
  }
  .subline {
    left: 277px; top: 127px; width: 643px; height: 53px;
    background: var(--band-light);
  }
  .subline__text { font-size: 22px; font-weight: 600; color: var(--ink); letter-spacing: 0.3px; }
  .promise {
    position: absolute; left: 300px; top: 188px; width: 600px; text-align: center;
    font-size: 88px; font-weight: 700; letter-spacing: 3px; line-height: 1.1;
    background: linear-gradient(180deg, var(--silver-hi) 0%, #e8e6dc 55%, var(--silver-lo) 100%);
    -webkit-background-clip: text; background-clip: text; color: transparent;
    filter: drop-shadow(3px 4px 3px rgba(0,0,0,0.75));
  }
  .callout {
    left: 333px; top: 307px; width: 520px; height: 80px;
    background: var(--band-dark);
    border-right: 3px solid rgba(40,40,30,0.8);
  }
  .callout__text { font-size: 31px; font-weight: 600; color: var(--callout-yellow); letter-spacing: 0.5px; text-shadow: 2px 2px 2px rgba(0,0,0,0.6); }
  .contact {
    left: 400px; top: 400px; width: 336px; height: 66px;
    background: var(--band-dark);
    clip-path: polygon(4% 0, 100% 0, 96% 100%, 0 100%);
  }
  .contact__text { font-size: 27px; font-weight: 500; color: var(--call-red); letter-spacing: 0.5px; }
</style>
</head>
<body>
  <main class="banner">
    <div class="banner__photo" role="img" aria-label="Golf putting green at sunset with a flagstick, ball and putter in the foreground"></div>

    <div class="band headline"><h1 class="headline__text">Make the Member</h1></div>
    <div class="band subline"><p class="subline__text">Desire to spread the cost of their annual subscriptions</p></div>
    <p class="promise">Safe,Reliable</p>
    <div class="band callout"><p class="callout__text">Talk to the club to find out how.</p></div>
    <div class="band contact"><p class="contact__text">Call us :1300 582 916</p></div>
  </main>
</body>
</html>
```